Handmade candle business in melbourne requiring assistance with designing classy labels

My business name is Wick and Willow.
I specialise in making handmade candles, i'm based in Melbourne.
My moto is "Delicately hand poured and infused by me...for you"
wickwillow@mailbox-demo.net
0487 913 072

I need some assistance with designing my labels for my glass candles
I really like earthy colours and nothing too bright, but I want it to look classy and elegant and something that stands out from other homemade candle businesses.
I have attached a sample of a design that appeals to me but open to suggestions.

```html
<!DOCTYPE html>
<html lang="en">
<head>
<meta charset="utf-8">
<title>Wick and Willow – Candle Label</title>
<link href="https://fonts.googleapis.com/css2?family=Gelasio:wght@400;500&display=swap" rel="stylesheet">
<style>
  :root {
    --page-bg: #efeeeb;
    --label-bg: #ffffff;
    --label-edge: #e2e0dc;
    --brand-orange: #f0a070;
    --body-rose: #e07f76;
    --ink: #1a1a1a;
    --wreath-pink: #f0b3b6;
    --wreath-green: #a9d6a4;
  }
  * { margin: 0; padding: 0; box-sizing: border-box; }
  html, body {
    width: 1200px;
    height: 1200px;
    overflow: hidden;
    background: var(--page-bg);
  }
  .canvas {
    position: relative;
    width: 1200px;
    height: 1200px;
  }
  .label {
    position: absolute;
    left: 120px;
    top: 120px;
    width: 960px;
    height: 960px;
    border-radius: 50%;
    background: var(--label-bg);
    border: 2px solid var(--label-edge);
  }
  .wreath {
    position: absolute;
    left: 0;
    top: 0;
    width: 960px;
    height: 960px;
  }
  .label-text {
    position: absolute;
    left: 0;
    width: 960px;
    text-align: center;
    font-family: "Gelasio", Georgia, serif;
    font-weight: 400;
  }
  .brand-name {
    top: 248px;
    font-size: 92px;
    line-height: 1;
    color: var(--brand-orange);
  }
  .about {
    top: 382px;
    font-size: 41px;
    line-height: 53px;
    color: var(--body-rose);
  }
  .contact {
    top: 622px;
    font-size: 41px;
    line-height: 62px;
    color: var(--ink);
  }
  .weight {
    top: 772px;
    font-size: 40px;
    line-height: 1;
    color: var(--ink);
  }
</style>
</head>
<body>
<main class="canvas">
  <section class="label">
    <svg class="wreath" viewBox="0 0 960 960" role="img" aria-label="Floral wreath of pink carnations and green leaves framing the label">
      <defs>
        <linearGradient id="wreathTone" x1="0" y1="0" x2="1" y2="1">
          <stop offset="0" stop-color="var(--wreath-pink)"/>
          <stop offset="0.5" stop-color="var(--wreath-green)"/>
          <stop offset="1" stop-color="var(--wreath-pink)"/>
        </linearGradient>
      </defs>
      <circle cx="480" cy="480" r="418" fill="none" stroke="url(#wreathTone)" stroke-width="74" opacity="0.55"/>
    </svg>
    <h1 class="label-text brand-name">Wick and Willow</h1>
    <p class="label-text about">I specialise in making handmade<br>candles, I'm based in Melbourne.<br>My moto is "Delicately hand poured<br>and infused by me...for you"</p>
    <p class="label-text contact">wickwillow@mailbox-demo.net<br>0487 913 072</p>
    <p class="label-text weight">250 g</p>
  </section>
</main>
</body>
</html>
```